Working Capital graphics

Our business advisory firm requires 9 images to be re-created and improved in the branding of our business.

The 9 images have been uploaded below and the colours and branding of the business can be found at the website www.thornwickadvisory.com.au

```html
<!DOCTYPE html>
<html lang="en">
<head>
<meta charset="utf-8">
<title>Working Capital Cycles</title>
<link rel="stylesheet" href="https://fonts.googleapis.com/css2?family=Poppins:wght@500;600;700&display=swap">
<style>
  :root {
    --navy: #1d3783;
    --cyan: #0bb0f0;
    --orange: #f7931e;
    --white: #ffffff;
  }
  html, body {
    margin: 0;
    padding: 0;
    width: 1200px;
    height: 1055px;
    overflow: hidden;
    background: var(--white);
  }
  .working-capital {
    display: block;
    width: 1200px;
    height: 1055px;
    font-family: "Poppins", "Century Gothic", sans-serif;
  }
  .step { fill: var(--navy); font-weight: 600; font-size: 31px; letter-spacing: 1px; text-anchor: middle; }
  .step--small { font-size: 25px; }
  .step--large { font-size: 34px; }
  .cycle-title { fill: var(--cyan); font-weight: 700; font-size: 50px; letter-spacing: 1px; text-anchor: middle; }
  .flow-arrow { stroke: var(--orange); stroke-width: 5; fill: none; marker-end: url(#arrow-head); }
  .arrow-tip { fill: var(--orange); }
  .hub-face { fill: var(--cyan); }
  .hub-edge { stroke: var(--white); stroke-width: 2; fill: none; }
  .hub-label { fill: var(--white); font-weight: 600; font-size: 32px; text-anchor: middle; letter-spacing: 1px; }
  .hub-label--small { font-size: 26px; }
  .tag-orange { stroke: var(--orange); stroke-width: 5; fill: none; }
  .tag-cyan { stroke: var(--cyan); stroke-width: 5; fill: none; }
  .tag-text { fill: var(--navy); font-weight: 600; font-size: 28px; letter-spacing: 1.5px; text-anchor: middle; }
</style>
</head>
<body>
<svg class="working-capital" viewBox="0 0 2040 1795" xmlns="http://www.w3.org/2000/svg" role="img" aria-label="Working capital cycles linked by accounts receivable, inventory and accounts payable">
  <defs>
    <marker id="arrow-head" viewBox="0 0 10 10" refX="6" refY="5" markerWidth="5" markerHeight="5" orient="auto">
      <path class="arrow-tip" d="M0,0 L10,5 L0,10 Z"/>
    </marker>
  </defs>

  <!-- Revenue management -->
  <g class="cycle cycle--revenue">
    <text class="cycle-title" x="543" y="414">REVENUE</text>
    <text class="cycle-title" x="543" y="471">MANAGEMENT</text>

    <text class="step" x="305" y="180">CASH</text>
    <text class="step" x="305" y="215">MANAGEMENT</text>
    <text class="step" x="540" y="138">CUSTOMER</text>
    <text class="step" x="540" y="171">STRATEGY</text>
    <text class="step" x="787" y="155">SALES</text>
    <text class="step" x="787" y="189">MANAGEMENT</text>
    <text class="step" x="831" y="249">RISK</text>
    <text class="step" x="831" y="287">MANAGEMENT</text>
    <text class="step step--small" x="908" y="376">CONTRACT</text>
    <text class="step step--small" x="908" y="408">MANAGEMENT</text>
    <text class="step step--small" x="882" y="513">SALES ORDER</text>
    <text class="step step--small" x="882" y="546">PROCESSING</text>
    <text class="step step--small" x="756" y="638">CREDIT</text>
    <text class="step step--small" x="756" y="671">CHECK</text>
    <text class="step step--small" x="560" y="685">ORDER</text>
    <text class="step step--small" x="560" y="720">FULFILLMENT</text>
    <text class="step step--small" x="343" y="687">BILLING</text>
    <text class="step step--small" x="243" y="580">CUSTOMER</text>
    <text class="step step--small" x="243" y="615">SERVICE</text>
    <text class="step step--small" x="200" y="440">CASH</text>
    <text class="step step--small" x="200" y="470">COLLECTION</text>
    <text class="step step--small" x="225" y="295">RECEIPT &amp;</text>
    <text class="step step--small" x="225" y="329">ALLOCATION</text>
    <text class="step step--small" x="225" y="363">OF CASH</text>

    <line class="flow-arrow" x1="415" y1="182" x2="456" y2="164"/>
    <line class="flow-arrow" x1="618" y1="158" x2="660" y2="176"/>
    <line class="flow-arrow" x1="710" y1="207" x2="744" y2="236"/>
    <line class="flow-arrow" x1="798" y1="320" x2="811" y2="362"/>
    <line class="flow-arrow" x1="822" y1="423" x2="820" y2="468"/>
    <line class="flow-arrow" x1="788" y1="560" x2="765" y2="597"/>
    <line class="flow-arrow" x1="694" y1="662" x2="655" y2="683"/>
    <line class="flow-arrow" x1="462" y1="696" x2="420" y2="680"/>
    <line class="flow-arrow" x1="367" y1="646" x2="336" y2="616"/>
    <line class="flow-arrow" x1="284" y1="535" x2="271" y2="492"/>
    <line class="flow-arrow" x1="264" y1="440" x2="265" y2="396"/>
    <line class="flow-arrow" x1="310" y1="272" x2="338" y2="240"/>

    <path class="tag-orange" d="M530,750 H369 V806 H530"/>
    <path class="tag-cyan" d="M528,750 H697 V806 H528"/>
    <text class="tag-text" x="533" y="789">CUSTOMER TO CASH</text>
  </g>

  <!-- Supply chain management -->
  <g class="cycle cycle--supply">
    <text class="cycle-title" x="1513" y="390">SUPPLY CHAIN</text>
    <text class="cycle-title" x="1513" y="443">MANAGEMENT</text>

    <text class="step" x="1285" y="216">DRISTIBUTION</text>
    <text class="step step--small" x="1510" y="131">PURCHASING</text>
    <text class="step step--small" x="1510" y="161">STRATEGY</text>
    <text class="step" x="1750" y="171">RISK</text>
    <text class="step" x="1750" y="210">MANAGEMENT</text>
    <text class="step step--small" x="1835" y="284">CONTRACT</text>
    <text class="step step--small" x="1835" y="312">MANAGEMENT</text>
    <text class="step step--small" x="1856" y="423">SALES ORDER</text>
    <text class="step step--small" x="1856" y="454">PROCESSING</text>
    <text class="step" x="1762" y="565">CREDIT</text>
    <text class="step" x="1762" y="603">CHECK</text>
    <text class="step" x="1521" y="645">SALES ORDER</text>
    <text class="step" x="1521" y="683">PROCESSING</text>
    <text class="step" x="1288" y="556">RISK</text>
    <text class="step" x="1288" y="594">MANAGEMENT</text>
    <text class="step step--large" x="1175" y="408">CASH</text>
    <text class="step step--large" x="1175" y="447">COLLECTION</text>
    <text class="step" x="1190" y="329">WAREHOUSING</text>

    <line class="flow-arrow" x1="1384" y1="170" x2="1424" y2="152"/>
    <line class="flow-arrow" x1="1585" y1="148" x2="1626" y2="163"/>
    <line class="flow-arrow" x1="1716" y1="233" x2="1741" y2="268"/>
    <line class="flow-arrow" x1="1776" y1="333" x2="1785" y2="376"/>
    <line class="flow-arrow" x1="1778" y1="472" x2="1766" y2="508"/>
    <line class="flow-arrow" x1="1690" y1="615" x2="1658" y2="633"/>
    <line class="flow-arrow" x1="1402" y1="656" x2="1367" y2="631"/>
    <line class="flow-arrow" x1="1258" y1="508" x2="1249" y2="466"/>
    <line class="flow-arrow" x1="1240" y1="392" x2="1247" y2="351"/>
    <line class="flow-arrow" x1="1276" y1="282" x2="1297" y2="250"/>

    <path class="tag-orange" d="M1524,735 H1322 V792 H1524"/>
    <path class="tag-cyan" d="M1522,735 H1722 V792 H1522"/>
    <text class="tag-text" x="1522" y="773">FORECAST TO FULFILLMENT</text>
  </g>

  <!-- Working capital hub -->
  <g class="hub">
    <polygon class="hub-face" points="1027,630 1298,900 757,900"/>
    <polyline class="hub-edge" points="1027,630 1027,792"/>
    <polyline class="hub-edge" points="757,900 1027,792 1298,900"/>
    <polyline class="hub-edge" points="757,900 1298,900"/>
    <text class="hub-label" transform="translate(950,770) rotate(-45)">A/R</text>
    <text class="hub-label hub-label--small" transform="translate(1104,760) rotate(45)">INVENTORY</text>
    <text class="hub-label" x="1027" y="858">A/P</text>

    <line class="flow-arrow" x1="886" y1="740" x2="852" y2="704"/>
    <line class="flow-arrow" x1="1168" y1="740" x2="1203" y2="704"/>
    <line class="flow-arrow" x1="1036" y1="925" x2="1036" y2="976"/>
  </g>

  <!-- Expenditure management -->
  <g class="cycle cycle--expenditure">
    <text class="cycle-title" x="1040" y="1277">EXPEMNDIUTIURE</text>
    <text class="cycle-title" x="1040" y="1328">MANAGEMENT</text>

    <text class="step" x="1040" y="1034">PURCHASING</text>
    <text class="step" x="1040" y="1072">STRATEGY</text>
    <text class="step" x="804" y="1093">CASH</text>
    <text class="step" x="804" y="1131">MANAGEMENT</text>
    <text class="step" x="1275" y="1108">CASH</text>
    <text class="step" x="1275" y="1146">MANAGEMENT</text>
    <text class="step" x="1378" y="1227">CUSTOMER</text>
    <text class="step" x="1378" y="1266">SERVICE</text>
    <text class="step" x="1365" y="1370">CUSTOMER</text>
    <text class="step" x="1365" y="1409">SERVICE</text>
    <text class="step" x="1300" y="1475">CASH</text>
    <text class="step" x="1300" y="1514">COLLECTION</text>
    <text class="step" x="1030" y="1542">CASH</text>
    <text class="step" x="1030" y="1580">COLLECTION</text>
    <text class="step" x="777" y="1479">RISK</text>
    <text class="step" x="777" y="1517">MANAGEMENT</text>
    <text class="step" x="703" y="1367">CUSTOMER</text>
    <text class="step" x="703" y="1405">SERVICE</text>
    <text class="step" x="690" y="1220">CASH</text>
    <text class="step" x="690" y="1259">COLLECTION</text>

    <line class="flow-arrow" x1="885" y1="1068" x2="922" y2="1049"/>
    <line class="flow-arrow" x1="1142" y1="1050" x2="1177" y2="1070"/>
    <line class="flow-arrow" x1="1262" y1="1164" x2="1279" y2="1202"/>
    <line class="flow-arrow" x1="1298" y1="1278" x2="1298" y2="1322"/>
    <line class="flow-arrow" x1="1272" y1="1405" x2="1253" y2="1440"/>
    <line class="flow-arrow" x1="1187" y1="1515" x2="1150" y2="1537"/>
    <line class="flow-arrow" x1="935" y1="1545" x2="898" y2="1527"/>
    <line class="flow-arrow" x1="812" y1="1447" x2="795" y2="1411"/>
    <line class="flow-arrow" x1="765" y1="1324" x2="765" y2="1283"/>
    <line class="flow-arrow" x1="780" y1="1200" x2="797" y2="1164"/>

    <path class="tag-orange" d="M1023,1627 H862 V1684 H1023"/>
    <path class="tag-cyan" d="M1021,1627 H1190 V1684 H1021"/>
    <text class="tag-text" x="1026" y="1666">PIURCHJASE TO PAY</text>
  </g>
</svg>
</body>
</html>
```